Mailer Postcard for Potential Bankruptcy Clients

The postcard will be printed at 8.5"x6" to abide by the specification at the following link: https://www.mailtrelbo.com/submitting-art/specs/. I want an attractive two sided post card that includes my logo (see attachment). The design would have to have room for the website address, phone number, two location addresses and give them information about a civil action pending against them (You are being sued in X county (case# xxyx). We can help.). I don't really like the visuals of the attached postcard, so please use as a general guide for what I am trying to do. Ultimately, I want an ad that gets people to call me so I can help them.

I also want it to be compatible with the website (LoanHarbor.Legal).

Target Market(s)

Potential bankruptcy clients.

Industry/Entity Type

Legal

Colors

Designer to choose colors to be used in the design.

Requirements
Must have
• Phone number, addresses, website, and place for text regarding pending legal action against the receiver. Should say something to the effect: You have a pending legal action in (county name) County (court name [superior, magistrate, ect.]). Let us help you deal with it responsibly.
• Please note the design specifications at this link:

```html
<!DOCTYPE html>
<html lang="en">
<head>
<meta charset="utf-8">
<title>LoanHarbor Law Group – Bankruptcy Mailer</title>
<link href="https://fonts.googleapis.com/css2?family=Titillium+Web:wght@300;400;600;700;900&display=swap" rel="stylesheet">
<style>
  :root{
    --green:#6dba85;
    --green-dark:#4f9e69;
    --green-tint:#e8f4ec;
    --ink:#2f3336;
    --ink-soft:#5b6166;
    --charcoal:#3b3e41;
    --paper:#ffffff;
    --panel:#e4e6e8;
    --stage:#eceeed;
  }
  *{box-sizing:border-box;margin:0;padding:0}
  html,body{width:1200px;height:776px;overflow:hidden}
  body{background:var(--stage);font-family:"Titillium Web",Arial,sans-serif;color:var(--ink);position:relative}

  .postcard{position:absolute;top:190px;width:560px;height:396px;background:var(--paper);overflow:hidden;box-shadow:0 4px 16px rgba(0,0,0,.12)}
  .postcard--front{left:30px}
  .postcard--back{left:610px}

  /* FRONT */
  .front-photo{position:absolute;left:0;top:64px;width:250px;height:332px;
    background:linear-gradient(160deg,#c9ced3 0%,#9aa3ab 40%,#b9c4b4 75%,#8f9d86 100%)}
  .brand{position:absolute;top:22px;right:26px;display:flex;align-items:center;gap:10px}
  .brand__dot{width:26px;height:26px;border-radius:50%;background:var(--green)}
  .brand__name{font-size:22px;font-weight:600;color:var(--green-dark);line-height:1}
  .headline{position:absolute;left:272px;top:72px;line-height:1}
  .headline__lead{font-size:36px;font-weight:700;color:var(--green);display:block}
  .headline__main{font-size:28px;font-weight:700;color:var(--ink);text-transform:uppercase;display:block;margin-top:4px;line-height:1.05}
  .promise-band{position:absolute;left:250px;right:0;top:200px;height:42px;background:var(--green);
    color:#fff;font-size:24px;font-weight:700;text-transform:uppercase;display:flex;align-items:center;padding-left:22px}
  .pitch{position:absolute;left:276px;top:254px;width:276px;font-size:18px;line-height:1.25;color:var(--ink)}
  .pitch__cta{display:block;margin-top:4px;font-weight:600;white-space:nowrap}
  .pitch__accent{color:var(--green);font-weight:700;text-transform:uppercase}
  .web-strip{position:absolute;left:250px;right:0;bottom:0;height:40px;background:var(--green);
    color:#fff;font-size:20px;font-weight:600;display:flex;align-items:center;padding-left:30px}
  .offer-badge{position:absolute;left:14px;bottom:16px;width:190px;height:190px}
  .offer-badge svg{position:absolute;inset:0}
  .offer-badge__text{position:absolute;inset:0;display:flex;flex-direction:column;justify-content:center;align-items:center;
    color:#fff;text-align:center;line-height:1}
  .offer-badge__title{font-size:22px;font-weight:700}
  .offer-badge__note{font-size:11px;font-weight:400;margin-top:6px}

  /* BACK */
  .qualify-banner{position:absolute;left:0;top:22px;width:340px;height:64px;background:var(--green);
    border-radius:0 10px 10px 0;color:#fff;font-size:22px;font-weight:700;line-height:1.05;padding:7px 20px}
  .intro{position:absolute;left:22px;top:94px;width:305px;font-size:10.5px;line-height:1.35;color:var(--ink-soft)}
  .benefits{position:absolute;left:22px;top:154px;list-style:none}
  .benefits li{display:flex;align-items:center;gap:8px;font-size:14px;line-height:1.3;color:var(--ink)}
  .benefits li.is-strong{font-weight:700}
  .benefits svg{width:12px;height:10px;flex:none}
  .legal-notice{position:absolute;left:22px;top:288px;width:276px;padding:5px 9px;background:var(--green-tint);
    border-left:3px solid var(--green);font-size:10px;line-height:1.3;color:var(--ink)}
  .legal-notice strong{font-weight:700}
  .disclaimer{position:absolute;left:0;bottom:0;width:300px;height:50px;background:var(--charcoal);
    color:#e2e4e5;font-size:8px;line-height:1.35;padding:7px 14px}
  .return-address{position:absolute;left:344px;top:22px;width:134px;font-style:normal;font-size:10px;line-height:1.3;color:var(--ink)}
  .return-address__name{display:block;font-weight:700;font-size:12px;margin-bottom:2px}
  .return-address__label{display:block;font-weight:600;color:var(--green-dark);margin-top:3px}
  .stamp-box{position:absolute;right:18px;top:18px;width:58px;height:68px;background:var(--panel)}
  .call{position:absolute;left:344px;top:128px}
  .call__row{display:flex;align-items:center;gap:8px;font-size:14px;color:var(--ink)}
  .call__icon{width:24px;height:24px;border-radius:50%;border:2px solid var(--green);display:flex;align-items:center;justify-content:center}
  .call__phone{font-size:30px;font-weight:700;color:var(--ink);line-height:1.1;margin-top:4px}
  .call__web{font-size:11px;letter-spacing:3px;color:var(--ink-soft)}
  .mailing-area{position:absolute;left:318px;top:236px;width:224px;height:142px;
    background:linear-gradient(180deg,#e9ebec,#dcdfe1)}
</style>
</head>
<body>

<section class="postcard postcard--front" aria-label="Postcard front">
  <div class="front-photo" role="img" aria-label="Photo of a stressed man in a suit holding his head, with rolls of dollar bills"></div>

  <div class="brand">
    <span class="brand__dot"></span>
    <span class="brand__name">LoanHarbor Law Group</span>
  </div>

  <h1 class="headline">
    <span class="headline__lead">Working Hard?</span>
    <span class="headline__main">Still having<br>money troubles?</span>
  </h1>

  <div class="promise-band">Bankruptcy can help.</div>

  <p class="pitch">Don't let them foreclose,<br>sue or garnish your wages!
    <span class="pitch__cta"><span class="pitch__accent">Call now</span> for a <span class="pitch__accent">Free</span> consultation.</span>
  </p>

  <div class="web-strip">Visit at www.LoanHarbor.Legal</div>

  <div class="offer-badge">
    <svg viewBox="0 0 190 190" aria-hidden="true">
      <polygon fill="#4a4d50" stroke="#fff" stroke-width="3"
        points="95,6 112,34 142,18 144,52 178,52 164,82 186,104 156,118 166,150 134,148 124,180 95,160 66,180 56,148 24,150 34,118 4,104 26,82 12,52 46,52 48,18 78,34"/>
    </svg>
    <div class="offer-badge__text">
      <span class="offer-badge__title">No Cash<br>Upfront<br>Options<br>for Filing*</span>
      <span class="offer-badge__note">See back for details.</span>
    </div>
  </div>
</section>

<section class="postcard postcard--back" aria-label="Postcard back">
  <h2 class="qualify-banner">If you qualify, you can file bankruptcy for $0 upfront!</h2>

  <p class="intro">If you're deep in debt and having trouble managing your mortgage and other bills, most law firms will recommend that you file for bankruptcy – without offering to help with fees. At Calloway &amp; Partners, we're different. We're here to help from start to finish.</p>

  <ul class="benefits">
    <li><svg viewBox="0 0 12 10"><path d="M1 5 L4.5 8.5 L11 1.5" fill="none" stroke="#6dba85" stroke-width="2"/></svg>Affordable Re-Payment Plans</li>
    <li><svg viewBox="0 0 12 10"><path d="M1 5 L4.5 8.5 L11 1.5" fill="none" stroke="#6dba85" stroke-width="2"/></svg>No-Money Down Options</li>
    <li><svg viewBox="0 0 12 10"><path d="M1 5 L4.5 8.5 L11 1.5" fill="none" stroke="#6dba85" stroke-width="2"/></svg>Evening &amp; Weekend Hours</li>
    <li><svg viewBox="0 0 12 10"><path d="M1 5 L4.5 8.5 L11 1.5" fill="none" stroke="#6dba85" stroke-width="2"/></svg>No Need to Miss Work!</li>
    <li><svg viewBox="0 0 12 10"><path d="M1 5 L4.5 8.5 L11 1.5" fill="none" stroke="#6dba85" stroke-width="2"/></svg>Child Friendly Office</li>
    <li class="is-strong"><svg viewBox="0 0 12 10"><path d="M1 5 L4.5 8.5 L11 1.5" fill="none" stroke="#6dba85" stroke-width="2"/></svg>Bankruptcy Expertise</li>
    <li class="is-strong"><svg viewBox="0 0 12 10"><path d="M1 5 L4.5 8.5 L11 1.5" fill="none" stroke="#6dba85" stroke-width="2"/></svg>It's All We Do!</li>
  </ul>

  <p class="legal-notice">You have a pending legal action in <strong>(County Name) County</strong>, <strong>(Court Name)</strong> Court, Case # <strong>XXXX-XX</strong>. Let us help you deal with it responsibly.</p>

  <p class="disclaimer">The choice of a lawyer is an important decision and should not be based solely on advertising. Calloway &amp; Partners is a debt relief agency helping people file for relief under the federal bankruptcy code.</p>

  <address class="return-address">
    <span class="return-address__name">LoanHarbor Law Group</span>
    <span class="return-address__label">Main Office</span>
    100 Main Street, Suite 200<br>City, ST 00000
    <span class="return-address__label">Branch Office</span>
    45 Oak Avenue<br>Town, ST 00000
  </address>

  <div class="stamp-box"></div>

  <div class="call">
    <div class="call__row">
      <span class="call__icon">
        <svg width="12" height="12" viewBox="0 0 24 24"><path fill="#6dba85" d="M6.6 10.8a15.1 15.1 0 0 0 6.6 6.6l2.2-2.2a1 1 0 0 1 1-.25 11.4 11.4 0 0 0 3.6.57 1 1 0 0 1 1 1V20a1 1 0 0 1-1 1A17 17 0 0 1 3 4a1 1 0 0 1 1-1h3.5a1 1 0 0 1 1 1c0 1.25.2 2.45.57 3.57a1 1 0 0 1-.25 1z"/></svg>
      </span>
      Call Today!
    </div>
    <div class="call__phone">123-456-7890</div>
    <div class="call__web">www.LoanHarbor.Legal</div>
  </div>

  <div class="mailing-area"></div>
</section>

</body>
</html>
```